Estate Planner needs an Ad for a local newsletter

I need an ad designed for my practice as an estate planning attorney. The ad will be in a newsletter that targets individuals over the age of 55. My ad is 7.5"W x 4.6"H (a half page ad) .
The wording should include:
Varnholt, Danielle

Danielle Varnholt

Wisdom Meets Planning
Your Estate, Your Legacy

After 23 years as a military spouse, moving our family of six across the country,
I learned the true value of careful planning. Today I help Palomar County's seniors protect what matters most – their family’s future and their life’s work.

I understand that your estate is more than just assets – it's a lifetime of wise
decisions, cherished memories, and dreams for your family's future.

Professional Estate Planning:
• Wills & Living Trusts • Healthcare Directives
• Power of Attorney • Asset Protection
• Probate Avoidance • Peace of Mind

Plus also needs to have my contact information:
RPV Law
Danielle Varnholt
Attorney/Of Counsel
4712 Cedarbrook Lane
Lakemont, Florida 39904
(555) 684-1093
dvarnholt@rpvlegalteam.example
Logo is attached.

```html
<!DOCTYPE html>
<html lang="en">
<head>
<meta charset="utf-8">
<title>Danielle Varnholt – Estate Planning Ad</title>
<link rel="stylesheet" href="https://fonts.googleapis.com/css2?family=Roboto:wght@400;500;700&display=swap">
<style>
  :root {
    --brand-blue: #2f3d86;
    --panel-blue: #3b4a8e;
    --deep-navy: #211f3c;
    --logo-navy: #1f2250;
    --stripe: #e9eaf3;
    --quote-bg: #f4f4f4;
    --ink: #1e1e24;
    --white: #ffffff;
  }
  * { margin: 0; padding: 0; box-sizing: border-box; }
  html, body { width: 1200px; height: 736px; overflow: hidden; background: var(--white); }
  body { font-family: 'Roboto', Arial, sans-serif; color: var(--ink); }
  .ad { position: relative; width: 1200px; height: 736px; overflow: hidden; background: var(--white); }

  .backdrop { position: absolute; inset: 0; }

  .header-name {
    position: absolute; left: 52px; top: 26px;
    font-size: 24.5px; font-weight: 700; color: var(--brand-blue); letter-spacing: -0.2px;
  }
  .header-rule { position: absolute; left: 0; top: 62px; width: 268px; height: 4px; background: var(--brand-blue); }
  .tagline { position: absolute; left: 52px; top: 74px; font-size: 13px; line-height: 19px; }

  .story {
    position: absolute; left: 33px; top: 143px; width: 690px; height: 162px;
    background: var(--quote-bg); padding: 9px 20px 0 21px;
  }
  .story p { font-size: 15.8px; line-height: 26.6px; text-align: justify; }
  .story .story-lead { margin-bottom: 14px; }
  .story .story-promise { font-weight: 700; text-align: left; }

  .logo {
    position: absolute; left: 922px; top: 18px; width: 248px;
    font-size: 46px; font-weight: 700; color: var(--logo-navy); text-align: center; letter-spacing: 1px;
  }

  .portrait { position: absolute; left: 636px; top: 76px; width: 552px; height: 660px; }

  .services { position: absolute; left: 0; top: 345px; width: 580px; height: 255px; color: var(--white); }
  .services h2 { position: absolute; left: 55px; top: 30px; font-size: 18.5px; font-weight: 700; }
  .service { position: absolute; display: flex; align-items: center; gap: 13px; font-size: 15px; }
  .service-icon {
    width: 46px; height: 46px; border-radius: 50%;
    background: rgba(255,255,255,0.14); display: flex; align-items: center; justify-content: center;
  }
  .service-icon svg { width: 26px; height: 26px; fill: none; stroke: var(--white); stroke-width: 1.5; stroke-linecap: round; stroke-linejoin: round; }

  .contact-card { position: absolute; left: 58px; top: 622px; color: var(--white); }
  .contact-card .firm { font-size: 14.5px; }
  .contact-card .name { font-size: 29px; font-weight: 700; margin-top: 6px; letter-spacing: -0.3px; }
  .contact-card .role { font-size: 14.5px; margin-top: 5px; }
  .contact-divider { position: absolute; left: 343px; top: 622px; width: 2px; height: 103px; background: var(--white); }

  .contact-list { position: absolute; left: 370px; top: 624px; color: var(--white); list-style: none; font-size: 15px; }
  .contact-list li { position: absolute; left: 0; display: flex; gap: 16px; white-space: nowrap; line-height: 16px; }
  .contact-list svg { width: 16px; height: 16px; fill: var(--white); flex: none; margin-top: 1px; }

  .ad-code { position: absolute; right: 36px; top: 710px; font-size: 8px; color: var(--white); }
</style>
</head>
<body>
<div class="ad">
  <svg class="backdrop" width="1200" height="736" viewBox="0 0 1200 736" aria-hidden="true">
    <defs>
      <linearGradient id="panelFill" x1="0" y1="0" x2="1" y2="1">
        <stop offset="0" stop-color="#46558f"/>
        <stop offset="1" stop-color="#38478a"/>
      </linearGradient>
    </defs>
    <g fill="var(--stripe)">
      <rect x="803" y="0" width="50" height="285"/>
      <rect x="880" y="0" width="50" height="285"/>
      <rect x="957" y="0" width="50" height="285"/>
      <rect x="1034" y="0" width="50" height="285"/>
      <rect x="1111" y="0" width="50" height="285"/>
    </g>
    <polygon points="982,285 1200,285 1200,540 982,540" fill="var(--panel-blue)"/>
    <polygon points="0,345 473,345 567,600 0,600" fill="url(#panelFill)"/>
    <polygon points="483,345 503,345 578,540 556,540" fill="var(--brand-blue)"/>
    <polygon points="548,540 1200,540 1200,736 0,736 0,600 567,600" fill="var(--deep-navy)"/>
  </svg>

  <div class="header-name">Danielle Varnholt</div>
  <div class="header-rule"></div>
  <p class="tagline">Wisdom Meets Planning<br>Your Estate, Your Legacy</p>

  <div class="story">
    <p class="story-lead">After 23 years as a military spouse, moving our family of six across the country, I learned the true value of careful planning. Today I help Palomar County's seniors protect what matters most – their family’s future and their life’s work.</p>
    <p class="story-promise">I understand that your estate is more than just assets – it's a lifetime of wise decisions, cherished memories, and dreams for your family's future.</p>
  </div>

  <div class="logo">RPV Law</div>

  <svg class="portrait" viewBox="0 0 552 660" role="img" aria-label="Portrait photo of Danielle Varnholt in a navy suit, smiling, arms folded">
    <defs>
      <linearGradient id="portraitFill" x1="0" y1="0" x2="0" y2="1">
        <stop offset="0" stop-color="#5b4a44"/>
        <stop offset="0.35" stop-color="#2f3a55"/>
        <stop offset="1" stop-color="#1c2438"/>
      </linearGradient>
    </defs>
    <path d="M140 60 Q200 0 300 20 Q370 40 390 160 L390 240 Q470 260 500 320 Q560 420 540 470 L470 520 L440 660 L10 660 L40 420 Q60 320 130 280 L150 250 Q60 200 140 60 Z" fill="url(#portraitFill)" opacity="0.92"/>
  </svg>

  <section class="services" role="img" aria-label="Background photo of an attorney meeting with clients, tinted blue">
    <h2>Professional Estate Planning:</h2>
    <div class="service" style="left:50px; top:68px;">
      <span class="service-icon"><svg viewBox="0 0 24 24"><path d="M6 3h10l3 3v15H6z"/><path d="M9 9h7M9 13h7M9 17h4"/></svg></span>Wills &amp; Living Trusts</div>
    <div class="service" style="left:279px; top:68px;">
      <span class="service-icon"><svg viewBox="0 0 24 24"><path d="M12 3l7 3v6c0 4-3 7-7 9-4-2-7-5-7-9V6z"/></svg></span>Asset Protection</div>
    <div class="service" style="left:50px; top:121px;">
      <span class="service-icon"><svg viewBox="0 0 24 24"><path d="M12 20s-7-4.5-7-10a4 4 0 0 1 7-2.5A4 4 0 0 1 19 10c0 5.5-7 10-7 10z"/><path d="M12 10v5M9.5 12.5h5"/></svg></span>Healthcare Directives</div>
    <div class="service" style="left:279px; top:121px;">
      <span class="service-icon"><svg viewBox="0 0 24 24"><rect x="3" y="7" width="16" height="12" rx="1"/><path d="M8 7V5h6v2"/><circle cx="18" cy="17" r="3.5"/></svg></span>Probate Avoidance</div>
    <div class="service" style="left:50px; top:174px;">
      <span class="service-icon"><svg viewBox="0 0 24 24"><circle cx="10" cy="8" r="3.5"/><path d="M4 21c0-4 3-7 6-7s6 3 6 7"/><rect x="15" y="3" width="6" height="4"/></svg></span>Power of Attorney</div>
    <div class="service" style="left:279px; top:174px;">
      <span class="service-icon"><svg viewBox="0 0 24 24"><circle cx="12" cy="13" r="6"/><path d="M9.5 14.5q2.5 2 5 0M12 3v2M6 5l1 1.5M18 5l-1 1.5"/></svg></span>Peace of Mind</div>
  </section>

  <div class="contact-card">
    <div class="firm">RPV Law</div>
    <div class="name">Danielle Varnholt</div>
    <div class="role">Attorney/Of Counsel</div>
  </div>
  <div class="contact-divider"></div>

  <ul class="contact-list">
    <li style="top:0;"><svg viewBox="0 0 24 24"><path d="M12 2a7 7 0 0 0-7 7c0 5 7 13 7 13s7-8 7-13a7 7 0 0 0-7-7zm0 9.5A2.5 2.5 0 1 1 12 6.5a2.5 2.5 0 0 1 0 5z"/></svg><span>4712 Cedarbrook Lane<br>Lakemont, Florida 39904</span></li>
    <li style="top:48px;"><svg viewBox="0 0 24 24"><path d="M6.6 10.8a15 15 0 0 0 6.6 6.6l2.2-2.2a1 1 0 0 1 1-.25 11.4 11.4 0 0 0 3.6.6 1 1 0 0 1 1 1V20a1 1 0 0 1-1 1A17 17 0 0 1 3 4a1 1 0 0 1 1-1h3.5a1 1 0 0 1 1 1c0 1.25.2 2.45.6 3.6a1 1 0 0 1-.25 1z"/></svg><span>(555) 684-1093</span></li>
    <li style="top:82px;"><svg viewBox="0 0 24 24"><path d="M2 6l10 7 10-7V5H2zM2 8v11h20V8l-10 7z"/></svg><span>dvarnholt@rpvlegalteam.example</span></li>
  </ul>

  <div class="ad-code">C38</div>
</div>
</body>
</html>
```